Learning platform for primary and secondary schools needs a new design

We need to restyle the website: www.pennaboschetto.org.
We are developing new functionalities that will enable to turn the platform in an interactive e-learning center for teachers, parents and pupils. Our target is providing contents and learning methods for primary and secondary school.
We want to give a new structure to the homepage and all menu sections and to find a new design that facilitates users to orientate themselves. We love our main picture and we would like to emphasize it. We like our logo and we don't want to change it.
The homepage should fulfil three main tasks:
- welcome visitors;
- encourage visitors to explore three areas of free contents: learning (scopri), experimenting (esperimenti), cooking (ricette)
- convert visitors in logged users (users can register as teachers, parents or students).
We also need a new design for:
- log-in page,
- slideshow,
- galleries of pictures,
- blog page,
- newsletter.
If you have any questions, do not hesitate to contact me.
Good job!
Giulia
Updates
Hi guys,
First of all I'd like to say thanks to all designers that submitted their ideas.
Up to now I didn't find any design that really convinced me, that's why I decided to share with you a design idea that could make easier your job (please see again the project briefing). I can't wait to see your new designs!
Good job
Ciao
Giuliabetta
Hi guys,
I would like to thank you for all your wonderful design proposals. We have just launched a friends and family voting pool to help us in getting the final decision. We'll let you know the result as soon as possible within tomorrow.
Ciao
Giuliabetta
Target Market(s)
Italian teachers, parents and students attending primary and secondary school
Industry/Entity Type
Cooking
Look and feel
Each slider illustrates characteristics of the customer's brand and the style your logo design should communicate.

```html
<!DOCTYPE html>
<html lang="it">
<head>
<meta charset="utf-8">
<title>PennaBoschetto – Home</title>
<link rel="stylesheet" href="https://fonts.googleapis.com/css2?family=Patrick+Hand&family=Roboto:wght@400;500&display=swap">
<style>
  :root{
    --sky-top:#3aa8e4;
    --sky-low:#8fd0f2;
    --orange:#f38b2c;
    --orange-light:#f9b27a;
    --ellipse:#d3e9f5;
    --ellipse-edge:#ffffff;
    --ink:#333333;
    --ink-soft:#5b5b5b;
    --grass:#5fa10d;
    --grass-light:#7ab823;
    --footer:#3b3b3b;
    --white:#ffffff;
    --hand:"Patrick Hand", cursive;
    --body:"Roboto", sans-serif;
  }
  *{box-sizing:border-box;margin:0;padding:0}
  html,body{width:823px;height:1200px;overflow:hidden}
  body{position:relative;font-family:var(--body);color:var(--ink);
    background:linear-gradient(#ffffff 504px,#e6f3fa 560px,#ffffff 700px,#f4f9fc 880px);}

  .top-band{position:absolute;left:0;top:0;width:823px;height:19px;background:var(--sky-top)}
  .hero{position:absolute;left:0;top:19px;width:823px;height:485px;
    background:linear-gradient(var(--sky-top) 0%,var(--sky-low) 60%,#e3b79b 80%,#f1dccd 100%);}
  .hero-illustration{position:absolute;left:10px;top:100px;width:810px;height:320px;
    background:linear-gradient(90deg,#f0a86a,#f6d28a 30%,#e7824a 55%,#f5c98a 80%,#eadfc8);
    border-radius:6px;opacity:.85}

  .nav{position:absolute;left:136px;top:19px;width:687px;height:40px;
    background:linear-gradient(var(--orange-light),var(--orange));}
  .nav a{position:absolute;top:12px;color:var(--white);font-size:13px;text-decoration:none;letter-spacing:.2px}

  .brand-corner{position:absolute;left:0;top:0;width:206px;height:180px}
  .brand{position:absolute;left:12px;top:46px;display:flex;align-items:center;gap:5px;
    font-family:var(--hand);font-size:14px;color:#8a5a2b}
  .brand-dot{width:9px;height:9px;border-radius:50%;background:#8a5a2b}

  .social{position:absolute;left:666px;top:69px;display:flex;gap:6px}
  .social span{width:27px;height:27px;border-radius:4px;display:block}

  .slider-arrows{position:absolute;left:725px;top:469px;display:flex;gap:3px}
  .slider-arrows span{width:18px;height:18px;border-radius:50%;border:1px solid #c9b8a8;
    background:#fff;color:#999;font-size:11px;line-height:16px;text-align:center}

  .welcome{position:absolute;left:143px;top:426px;width:542px;height:157px;border-radius:50%;
    background:var(--ellipse);border:3px solid var(--ellipse-edge);box-shadow:0 2px 6px rgba(0,0,0,.15);
    text-align:center;padding-top:22px}
  .welcome h1{font-family:var(--hand);font-weight:400;font-size:21px;letter-spacing:1px;color:#555}
  .welcome p{margin:8px auto 0;width:470px;font-size:13.4px;line-height:21.5px;color:var(--ink-soft)}

  .card{position:absolute;top:684px;width:223px;height:162px;border:3px solid var(--white);
    box-shadow:0 1px 4px rgba(0,0,0,.2)}
  .card-scopri{left:57px;background:linear-gradient(135deg,#cfe3c7,#bcd6c0)}
  .card-esperimenti{left:300px;background:linear-gradient(135deg,#c9def0,#d7cde8)}
  .card-ricette{left:543px;background:linear-gradient(135deg,#cde7cf,#dbe7c4)}
  .card-head{position:absolute;left:19px;top:-52px;width:180px;height:85px;border-radius:50%;
    background:var(--ellipse);border:3px solid var(--white);box-shadow:0 2px 4px rgba(0,0,0,.15);
    font-family:var(--hand);font-size:21px;letter-spacing:1px;text-align:center;line-height:80px;color:#222}
  .card p{position:absolute;left:39px;top:51px;width:170px;font-size:11.6px;line-height:19.6px;color:#222}
  .card .more{position:absolute;right:14px;bottom:10px;width:20px;height:18px}

  .skyline{position:absolute;left:0;top:875px;width:823px;height:45px;
    background:linear-gradient(transparent,rgba(160,180,195,.35))}
  .meadow{position:absolute;left:0;top:905px;width:823px;height:143px;
    background:linear-gradient(var(--grass-light),var(--grass) 30%)}
  .role{position:absolute;top:946px;width:200px;text-align:center;font-family:var(--hand);
    font-size:17px;letter-spacing:1px;color:var(--white)}
  .enter{position:absolute;top:980px;width:131px;height:45px;border-radius:50%;
    background:linear-gradient(#f9a35a,var(--orange));box-shadow:0 2px 4px rgba(0,0,0,.25);
    color:var(--white);font-size:12.5px;font-weight:500;text-align:center;line-height:45px}

  .partners{position:absolute;left:0;top:1048px;width:823px;height:92px;background:var(--white);
    border-bottom:3px solid var(--grass-light);display:flex;align-items:center;justify-content:space-around;padding:0 50px}
  .partner{background:#d9dde2}
  .partner.round{width:64px;height:64px;border-radius:50%}
  .partner.wide{width:118px;height:44px;border-radius:4px}
  .partner.small{width:52px;height:52px;border-radius:6px}

  .footer{position:absolute;left:0;top:1143px;width:823px;height:57px;background:var(--footer);
    color:var(--white);font-size:10.5px;text-align:center;line-height:57px}
</style>
</head>
<body>
  <div class="top-band"></div>
  <section class="hero">
    <div class="hero-illustration" role="img" aria-label="Illustrated street of colourful Italian shops: greengrocer, bakery, dairy, butcher and fishmonger"></div>
  </section>

  <nav class="nav">
    <a href="#" style="left:100px">IL PROGRAMMA</a>
    <a href="#" style="left:254px">IL PROGETTO DI RICERCA</a>
    <a href="#" style="left:454px">CHI SIAMO</a>
    <a href="#" style="left:567px">SOSTIENI</a>
  </nav>

  <svg class="brand-corner" viewBox="0 0 206 180" aria-hidden="true">
    <polygon points="0,0 206,0 0,180" fill="#ffffff"/>
  </svg>
  <div class="brand"><span class="brand-dot"></span>PennaBoschetto</div>

  <div class="social" aria-label="Social">
    <span style="background:#3b5fa0"></span>
    <span style="background:#d54a36"></span>
    <span style="background:#d22a2a"></span>
  </div>

  <div class="slider-arrows"><span>‹</span><span>›</span></div>

  <section class="welcome">
    <h1>BENVENUTI</h1>
    <p>PennaBoschetto® è un progetto sperimentale di didattica della scienza in cui il cibo è proposto come strumento per stimolare il pensiero scientifico e la consapevolezza di quanto sia importante un’alimentazione sana.</p>
  </section>

  <article class="card card-scopri" role="img" aria-label="Faded greengrocer illustration behind the Scopri card">
    <div class="card-head">SCOPRI</div>
    <p>Lorem ipsum lorem ipsum lorem ipsum lorem ipsum lorem ipsum lorem ipsum lorem ipsum lorem ipsum</p>
    <svg class="more" viewBox="0 0 20 18"><path d="M2 2l7 7-7 7M10 2l7 7-7 7" fill="none" stroke="#333" stroke-width="2.6"/></svg>
  </article>
  <article class="card card-esperimenti" role="img" aria-label="Faded snowflake crystal pattern behind the Esperimenti card">
    <div class="card-head">ESPERIMENTI</div>
    <p>Lorem ipsum lorem ipsum lorem ipsum lorem ipsum lorem ipsum lorem ipsum lorem ipsum lorem ipsum</p>
    <svg class="more" viewBox="0 0 20 18"><path d="M2 2l7 7-7 7M10 2l7 7-7 7" fill="none" stroke="#333" stroke-width="2.6"/></svg>
  </article>
  <article class="card card-ricette" role="img" aria-label="Faded vegetable illustration behind the Ricette card">
    <div class="card-head">RICETTE</div>
    <p>Lorem ipsum lorem ipsum lorem ipsum lorem ipsum lorem ipsum lorem ipsum lorem ipsum lorem ipsum</p>
    <svg class="more" viewBox="0 0 20 18"><path d="M2 2l7 7-7 7M10 2l7 7-7 7" fill="none" stroke="#333" stroke-width="2.6"/></svg>
  </article>

  <div class="skyline" role="img" aria-label="Faint city skyline on the horizon"></div>
  <section class="meadow">
    <svg width="823" height="20" viewBox="0 0 823 20" style="position:absolute;top:-8px;left:0" aria-hidden="true">
      <path d="M0 12 Q200 0 420 10 T823 8 V20 H0Z" fill="#7ab823"/>
    </svg>
  </section>
  <div class="role" style="left:64px">SONO UN INSEGNANTE</div>
  <div class="role" style="left:310px">SONO UN INSEGNANTE</div>
  <div class="role" style="left:553px">SONO UN GENITORE</div>
  <div class="enter" style="left:97px">ENTRA</div>
  <div class="enter" style="left:343px">ENTRA</div>
  <div class="enter" style="left:591px">ENTRA</div>

  <section class="partners" aria-label="Partner">
    <span class="partner round"></span>
    <span class="partner wide"></span>
    <span class="partner wide" style="width:96px"></span>
    <span class="partner wide" style="width:104px"></span>
    <span class="partner round"></span>
    <span class="partner wide" style="width:76px"></span>
    <span class="partner small"></span>
  </section>

  <footer class="footer">© 2014 PENNABOSCHETTO SRL – start-up innovativa a vocazione sociale</footer>
</body>
</html>
```